3 x DIN A4 Flyer, Vorder- und Rückseite
Zielgruppe
Handwerksunternehmen
Aufgabenstellung
Wir benötigen 3 Werbeflyer die in Zeitschriften beigelegt werden. Jeweils DIN A4, Vorderseite beschreibt das Produkt, Rückseite kann zur Bestellung mittels Faxantwort benutzt werden. Profibilder und Text wird vollständig geliefert.

```html
<!DOCTYPE html>
<html lang="de">
<head>
<meta charset="utf-8">
<title>Prospektbox für die Baustelle – Flyer Vorder- und Rückseite</title>
<link rel="stylesheet" href="https://fonts.googleapis.com/css2?family=Source+Sans+3:wght@400;600;700&display=swap">
<style>
  :root {
    --stage: #e9ecef;
    --sky-light: #e6f2fb;
    --sky: #b9dcf3;
    --sky-deep: #8cc3ea;
    --navy: #2a4c8c;
    --navy-dark: #1f3a72;
    --orange: #f39a1e;
    --ink: #34465e;
    --line: #8fa9c4;
    --white: #ffffff;
  }
  * { box-sizing: border-box; margin: 0; padding: 0; }
  html, body { width: 1200px; height: 800px; overflow: hidden; }
  body {
    background: var(--stage);
    font-family: "Source Sans 3", "Segoe UI", sans-serif;
    color: var(--ink);
    position: relative;
  }
  .sheet {
    position: absolute; top: 30px; width: 524px; height: 740px;
    background: linear-gradient(160deg, var(--sky-light) 0%, var(--sky) 55%, var(--sky-deep) 100%);
    box-shadow: 0 6px 18px rgba(40,60,90,.25);
    overflow: hidden;
  }
  .sheet--front { left: 46px; }
  .sheet--back { left: 630px; }
  .sheet__bands { position: absolute; inset: 0; width: 100%; height: 100%; }
  .abs { position: absolute; }

  /* Front */
  .headline { left: 28px; top: 72px; font-size: 40px; font-weight: 700; color: var(--navy); letter-spacing: -.5px; }
  .subline { right: 36px; top: 130px; font-size: 28px; font-weight: 700; color: var(--orange); }
  .product-photo { left: 22px; top: 200px; width: 220px; height: 390px; border-radius: 4px;
    background: linear-gradient(180deg, rgba(255,255,255,.85), rgba(220,235,248,.6)); }
  .price { left: 0; top: 440px; width: 210px; height: 52px;
    background: linear-gradient(180deg, #ffffff, #d8ecfa); border-radius: 0 10px 10px 0;
    box-shadow: 0 2px 6px rgba(40,70,120,.3); display: flex; align-items: center; justify-content: center; gap: 6px; }
  .price__amount { font-size: 30px; font-weight: 700; color: var(--navy); }
  .price__unit { font-size: 12px; font-weight: 700; color: var(--navy); line-height: 1; }
  .price__unit small { display: block; font-size: 8px; }
  .features { left: 256px; top: 268px; width: 250px; font-size: 11px; line-height: 22px; list-style: none; }
  .features li { padding-left: 16px; position: relative; }
  .features li.plus::before { content: "+"; position: absolute; left: 0; top: 0; font-weight: 700; color: var(--navy); font-size: 14px; }
  .features b { color: var(--navy); font-weight: 700; }
  .info-panel { left: 130px; top: 570px; width: 380px; height: 100px; padding: 14px 16px 0 44px;
    background: rgba(255,255,255,.45); border-radius: 8px; transform: rotate(-3deg); font-size: 10.5px; line-height: 16px; }
  .info-panel p { position: relative; margin-bottom: 10px; }
  .info-panel p::before { content: "→"; position: absolute; left: -28px; top: -1px; color: var(--navy); font-weight: 700; font-size: 14px; }
  .footnote { left: 20px; right: 20px; top: 686px; text-align: center; font-size: 8.5px; line-height: 12px; }
  .imprint { left: 20px; right: 20px; top: 718px; text-align: center; font-size: 8.5px; }

  /* Back */
  .order-title { left: 26px; top: 28px; font-size: 30px; font-weight: 700; color: var(--navy); }
  .order-fax { right: 20px; top: 104px; font-size: 24px; font-weight: 700; color: var(--orange); transform: rotate(-3deg); }
  .form-panel { left: 12px; top: 148px; width: 500px; height: 580px; background: rgba(255,255,255,.3); border-radius: 10px; }
  .label { font-size: 10px; color: var(--ink); }
  .label--head { font-size: 11px; font-weight: 700; color: var(--navy); }
  .recipient { font-size: 9px; line-height: 12px; }
  .field { left: 18px; width: 470px; border-bottom: 1px solid var(--line); height: 22px; font-size: 10px; padding-top: 0; }
  .qty-box { left: 18px; top: 568px; width: 96px; height: 34px; background: var(--white); }
  .qty-label { left: 126px; top: 580px; font-size: 11px; font-weight: 600; }
</style>
</head>
<body>

<section class="sheet sheet--front" aria-label="Flyer Vorderseite">
  <svg class="sheet__bands" viewBox="0 0 524 740" aria-hidden="true">
    <polygon points="0,60 524,40 524,58 0,78" fill="#ffffff" opacity=".55"/>
    <polygon points="0,118 524,100 524,170 0,190" fill="#ffffff" opacity=".35"/>
    <polygon points="0,184 524,166 524,172 0,190" fill="#ffffff" opacity=".8"/>
    <polygon points="0,560 524,520 524,740 0,740" fill="#ffffff" opacity=".12"/>
  </svg>
  <h1 class="abs headline">Prospektbox</h1>
  <p class="abs subline">für die Baustelle</p>
  <div class="abs product-photo" role="img" aria-label="Foto der transparenten Prospektbox mit Deckel"></div>
  <div class="abs price"><span class="price__amount">26,–</span><span class="price__unit">EUR*<small>(netto)</small></span></div>
  <ul class="abs features">
    <li>Mit einem Klick erwerben Sie zu einem</li>
    <li class="plus"><b>absoluten Sonderpreis</b> die neue und</li>
    <li class="plus"><b>wetterfeste</b></li>
    <li class="plus"><b>DIN A4 Hochformat Prospektbox mit Deckel</b></li>
    <li class="plus"><b>zur Wandmontage</b> (Montage-Schrauben sind</li>
    <li>im Lieferumfang NICHT enthalten)</li>
    <li class="plus"><b>oder Pfostenmontage mittels</b></li>
    <li><b>Kunststoffbinder</b> (im Lieferumfang enthalten)</li>
    <li>und Hohlkehle an der Rückseite des Displays.</li>
  </ul>
  <div class="abs info-panel">
    <p>Die ideale Aussenbox für die Präsentation Ihrer Flyer, Prospekte und Informationen in allen Aussenbereichen.</p>
    <p>Ihre Werbemittel werden durch einen Deckel vor Nässe geschützt. Bohrungen für die Wandmontage vorhanden.</p>
  </div>
  <p class="abs footnote">* Alle angegebenen Preise verstehen sich in Euro zzgl. der gesetzlichen geltenden Mehrwertsteuer von derzeit 19%.<br>Die Lieferung erfolgt ca. 10 Tage nach Bestelleingang. Porto/Verpackung 6,90 Euro</p>
  <p class="abs imprint">Fördergesellschaft des Dach- und Holzhandwerks mbH • Birkenauer Straße 42 • 80999 München • www.kltr.de</p>
</section>

<section class="sheet sheet--back" aria-label="Flyer Rückseite Faxbestellung">
  <svg class="sheet__bands" viewBox="0 0 524 740" aria-hidden="true">
    <polygon points="0,0 524,0 524,56 0,86" fill="#ffffff" opacity=".5"/>
    <polygon points="0,84 524,54 524,62 0,92" fill="#ffffff" opacity=".85"/>
    <polygon points="0,100 524,80 524,150 0,170" fill="#ffffff" opacity=".3"/>
  </svg>
  <h2 class="abs order-title">bestellen Sie einfach</h2>
  <p class="abs order-fax">per Fax 040 52917-300</p>
  <div class="abs form-panel"></div>
  <span class="abs label label--head" style="left:28px;top:150px">Empfänger</span>
  <p class="abs recipient" style="left:180px;top:150px">KLTR mbH<br><br>Birkenauer Straße 42<br>80999 München</p>
  <p class="abs recipient" style="left:350px;top:150px">Telefon:&nbsp; 040 52917-340<br>Fax:&nbsp;&nbsp;&nbsp;&nbsp;&nbsp;&nbsp;&nbsp; 040 52917-300<br><br>Ansprechpartner: Jonas Berthold</p>
  <span class="abs label label--head" style="left:18px;top:232px">Besteller</span>
  <div class="abs field" style="top:262px">Firmenname</div>
  <div class="abs field" style="top:300px">Name, Vorname</div>
  <div class="abs field" style="top:338px">Straße, Hausnummer</div>
  <div class="abs field" style="top:376px">PLZ, Ort</div>
  <div class="abs field" style="top:412px;height:44px">Telefon</div>
  <div class="abs field" style="top:474px">Unterschrift/Stempel</div>
  <div class="abs field" style="top:514px">Sie sind in welcher Innung Mitglied?</div>
  <div class="abs qty-box"></div>
  <span class="abs qty-label">Anzahl der gewünschten Menge</span>
  <div class="abs field" style="top:636px">Bemerkungen:</div>
</section>

</body>
</html>
```